Church Bulletin Ad (see attached sample)

Create a New Church Bulletin Ad. I have attached some samples of what we would like to have in the ad. (1) Marrowfield Realty Thorne Logo (2) Headshot (3) Lena Vasko & Greta Vasko, Real Estate Team (4) Phone number (5) Email address (6) St Aldwin Parishioners for over 40 Years. We would like for the ad to be clean and modern. NO OTHER IMAGES besides headshots and Marrowfield Realty Thorne Logo.

Target Market(s)

Church community

Industry/Entity Type

Real Estate

Font styles to use
Sans Serif
Other font styles liked:
• Modern Font

Colors
0054AA
0677BA
7BADD7
CADEEF
E8F1F8

Requirements
Must have
• Marrowfield Realty Thorne Logo; Headshot; Ad size is 4.5"x1.62"

```html
<!DOCTYPE html>
<html lang="en">
<head>
<meta charset="utf-8">
<title>St Aldwin Bulletin Ad – Vasko Real Estate Team</title>
<link rel="stylesheet" href="https://fonts.googleapis.com/css2?family=Montserrat:wght@600;700;800;900&display=swap">
<style>
  :root {
    --navy: #0b1a4a;
    --charcoal: #3b3b3e;
    --white: #ffffff;
    --backdrop: #dcdcdc;
    --photo-warm: #c7a58c;
    --photo-cool: #b9c3cf;
  }
  * { box-sizing: border-box; margin: 0; padding: 0; }
  html, body {
    width: 1136px; height: 1200px; overflow: hidden;
    background: var(--backdrop);
    font-family: "Montserrat", Arial, sans-serif;
  }
  .bulletin-ad {
    position: absolute; left: 48px; top: 413px;
    width: 1040px; height: 374px;
    background: var(--white);
    box-shadow: 0 4px 10px rgba(0,0,0,.25);
    overflow: hidden;
  }
  .headline-band {
    position: absolute; left: 0; top: 0; width: 100%; height: 93px;
    background: var(--navy); color: var(--white);
    display: flex; align-items: center; justify-content: center;
    font-weight: 700; font-size: 46px; letter-spacing: 3px;
  }
  .footer-band {
    position: absolute; left: 0; top: 297px; width: 100%; height: 77px;
    background: var(--charcoal);
  }
  .team-plate {
    position: absolute; left: 528px; top: 297px; width: 475px; height: 57px;
    background: var(--white); text-align: center;
    font-weight: 700; line-height: 1.2;
  }
  .team-names { color: var(--charcoal); font-size: 22px; margin-top: 1px; letter-spacing: .5px; }
  .team-title { color: var(--navy); font-size: 23px; letter-spacing: 1px; }
  .brand-tile {
    position: absolute; left: 36px; top: 270px; width: 101px; height: 88px;
    background: var(--navy); border: 4px solid var(--white);
    box-shadow: 0 1px 3px rgba(0,0,0,.3);
    display: flex; align-items: center; justify-content: center; text-align: center;
    color: var(--white); font-weight: 700; font-size: 12px; line-height: 1.25; padding: 4px;
  }
  .phone-line {
    position: absolute; left: 166px; top: 311px;
    display: flex; align-items: center; gap: 14px;
    color: var(--white); font-weight: 700; font-size: 36px; letter-spacing: 1px;
  }
  .phone-line svg { width: 28px; height: 28px; }
  .years-mark {
    position: absolute; left: 36px; top: 132px; color: var(--navy);
  }
  .years-number { font-weight: 900; font-size: 122px; line-height: 1; letter-spacing: -4px; }
  .years-ordinal { position: absolute; left: 156px; top: 10px; font-weight: 800; font-size: 26px; }
  .years-word { position: absolute; left: 72px; top: 82px; font-weight: 800; font-size: 24px; letter-spacing: -1px; background: var(--white); padding: 0 2px; }
  .parish-line {
    position: absolute; left: 240px; top: 146px;
    color: var(--charcoal); font-weight: 800; font-size: 34px; line-height: 1.02; letter-spacing: 1px;
  }
  .headshot {
    position: absolute; top: 113px; height: 163px;
    border: 3px solid var(--navy);
  }
  .headshot--lena { left: 573px; width: 181px; background: linear-gradient(180deg, #f1ece8, var(--photo-warm)); }
  .headshot--greta { left: 795px; width: 177px; background: linear-gradient(180deg, #dfe4ea, var(--photo-cool)); }
</style>
</head>
<body>
  <section class="bulletin-ad">
    <header class="headline-band">ENERGY EXCELLENCE EXPERIENCE</header>

    <div class="years-mark">
      <div class="years-number">40</div>
      <span class="years-ordinal">th</span>
      <span class="years-word">YEARS</span>
    </div>
    <p class="parish-line">ST. ALDWIN<br>PARISHIONERS<br>FOR OVER</p>

    <div class="headshot headshot--lena" role="img" aria-label="Headshot of Lena Vasko"></div>
    <div class="headshot headshot--greta" role="img" aria-label="Headshot of Greta Vasko"></div>

    <div class="footer-band"></div>
    <div class="team-plate">
      <p class="team-names">LENA VASKO &amp; GRETA VASKO</p>
      <p class="team-title">REAL ESTATE TEAM</p>
    </div>

    <div class="brand-tile">Marrowfield Realty Thorne</div>

    <p class="phone-line">
      <svg viewBox="0 0 24 24" aria-hidden="true"><path fill="#fff" d="M6.6 10.8a15.1 15.1 0 0 0 6.6 6.6l2.2-2.2c.3-.3.7-.4 1-.2 1.1.4 2.3.6 3.6.6.6 0 1 .4 1 1V20c0 .6-.4 1-1 1A17 17 0 0 1 3 4c0-.6.4-1 1-1h3.5c.6 0 1 .4 1 1 0 1.2.2 2.4.6 3.6.1.3 0 .7-.2 1z"/><path fill="none" stroke="#fff" stroke-width="1.8" stroke-linecap="round" d="M14.5 3.5a6 6 0 0 1 6 6M14.5 7a2.5 2.5 0 0 1 2.5 2.5"/></svg>
      206-555-0148
    </p>
  </section>
</body>
</html>
```